Word document template for sales proposals

I am after a template that is simple but impactful. Use of colour to be limited but some for impact would be good. The proposals are for use in the professional technical field.

```html
<!DOCTYPE html>
<html lang="en">
<head>
<meta charset="utf-8">
<title>Sales Proposal</title>
<link href="https://fonts.googleapis.com/css2?family=Lato:wght@400;700&family=Open+Sans:wght@400;700&display=swap" rel="stylesheet">
<style>
  :root {
    --brand-blue: #29a8e0;
    --brand-orange: #f7941d;
    --ink: #0a0a0a;
    --paper: #ffffff;
    --photo-steel: #7d8890;
    --photo-navy: #3f5a80;
  }
  * { margin: 0; padding: 0; box-sizing: border-box; }
  html, body { width: 849px; height: 1200px; overflow: hidden; background: var(--paper); }
  .cover {
    position: relative;
    width: 849px;
    height: 1200px;
    overflow: hidden;
    font-family: "Open Sans", sans-serif;
    background: var(--paper);
  }
  .cover__art { position: absolute; inset: 0; width: 849px; height: 1200px; }
  .year {
    position: absolute; left: 227px; top: 340px; width: 200px;
    text-align: center; color: var(--paper);
    font-size: 64px; line-height: 1; font-weight: 400;
  }
  .title {
    position: absolute; left: 398px; top: 448px;
    color: var(--ink); line-height: 0.95; font-size: 58px;
  }
  .title__light { display: block; font-weight: 400; }
  .title__bold { display: block; font-weight: 700; }
  .brand {
    position: absolute; left: 630px; top: 194px; width: 196px; height: 196px;
    display: flex; flex-direction: column; align-items: center; justify-content: center; gap: 10px;
  }
  .brand__dot { width: 34px; height: 34px; border-radius: 50%; background: var(--brand-orange); }
  .brand__name {
    color: var(--brand-orange); font-weight: 700; font-size: 19px; letter-spacing: 1px;
  }
  .details {
    position: absolute; left: 78px; width: 500px; text-align: center; color: var(--paper);
  }
  .details__label { top: 646px; font-size: 24px; }
  .details__client { top: 696px; font-size: 38px; }
  .details__client-co { top: 750px; font-size: 22px; letter-spacing: 0.3px; }
  .details__prepared { top: 813px; font-size: 26px; }
  .details__author { top: 863px; font-size: 38px; }
  .details__role { top: 918px; font-size: 16.5px; letter-spacing: 0.3px; }
  .contact {
    position: absolute; left: 78px; top: 952px; width: 500px;
    text-align: center; color: var(--paper); font-size: 16.5px; line-height: 25.5px; letter-spacing: 0.3px;
  }
  .footnote {
    position: absolute; left: 20px; top: 1102px; width: 809px;
    text-align: center; color: var(--paper); font-size: 12.2px;
  }
</style>
</head>
<body>
<main class="cover">
  <svg class="cover__art" viewBox="0 0 1241 1754" preserveAspectRatio="none" aria-hidden="false">
    <defs>
      <linearGradient id="photoTop" x1="0" y1="0" x2="1" y2="1">
        <stop offset="0" stop-color="#9aa3aa"/>
        <stop offset="1" stop-color="#5c656c"/>
      </linearGradient>
      <linearGradient id="photoLeft" x1="0" y1="0" x2="1" y2="1">
        <stop offset="0" stop-color="#8a8f94"/>
        <stop offset="0.6" stop-color="#3f5a80"/>
        <stop offset="1" stop-color="#2c3f5c"/>
      </linearGradient>
    </defs>
    <polygon class="photo photo--rigging" role="img" aria-label="Photo: technician in hard hat and safety vest working on rigging aboard a vessel"
      points="105,330 360,75 770,75 460,385 400,445 318,520" fill="url(#photoTop)"/>
    <polygon class="photo photo--technician" role="img" aria-label="Photo: engineer in blue workwear inspecting an industrial cleaning spray can"
      points="0,440 90,355 300,560 460,715 90,1100 0,1010" fill="url(#photoLeft)"/>
    <polygon class="band band--year" points="478,393 637,552 478,712 318,552" fill="var(--brand-orange)"/>
    <polygon class="band band--main" points="0,1220 478,745 1241,1508 1241,1710 1197,1754 0,1754" fill="var(--brand-blue)"/>
    <polygon class="band band--side" points="1035,75 1093,75 1093,1332 1035,1278" fill="var(--brand-blue)"/>
    <circle class="brand-ring" cx="1064" cy="427" r="143" fill="var(--paper)" stroke="var(--brand-blue)" stroke-width="5"/>
  </svg>

  <div class="year">2023</div>

  <h1 class="title">
    <span class="title__light">SALES</span>
    <span class="title__bold">PROPOSAL</span>
  </h1>

  <div class="brand">
    <span class="brand__dot"></span>
    <span class="brand__name">NORTHWIND</span>
  </div>

  <p class="details details__label">FOR</p>
  <p class="details details__client">[CLIENT NAME]</p>
  <p class="details details__client-co">Company Name of Client</p>
  <p class="details details__prepared">PREPARED BY:</p>
  <p class="details details__author">[YOUR NAME]</p>
  <p class="details details__role">Business Development Manager</p>

  <address class="contact" style="font-style: normal;">
    [Company Name Here]<br>
    [company address goes here, City State, Zip Code]<br>
    [123-456-7890] | [123-456-9999]<br>
    [manager@northwindfield.com]
  </address>

  <p class="footnote">This sales proposal contains all details relevant to scope of work, pricing, and terms as requested by [Client.FirstName] [Client.LastName]</p>
</main>
</body>
</html>
```